Copper Lantern

Please see attached Word document for requirements. I want the website to be one page.

Coding

Coded - Design and coding required

Number of Pages Required

1 page

Colors
0054AA
0677BA
7BADD7
CADEEF
E8F1F8

```html
<!DOCTYPE html>
<html lang="en">
<head>
<meta charset="utf-8">
<title>Copper Lantern — AI Workforce Scheduling</title>
<link href="https://fonts.googleapis.com/css2?family=Syne:wght@700;800&family=Inter:wght@400;500;600;700&display=swap" rel="stylesheet">
<style>
:root{
  --bg:#050c1c;
  --bg-deep:#040a17;
  --panel:#0c1830;
  --panel-2:#0f1d38;
  --line:#1b2a47;
  --line-soft:#142240;
  --blue-900:#0054AA;
  --blue-700:#0677BA;
  --blue-500:#1a8fe0;
  --blue-300:#7BADD7;
  --blue-100:#CADEEF;
  --blue-50:#E8F1F8;
  --text:#ffffff;
  --muted:#8a9bb8;
  --dim:#5d6f8f;
  --green:#2ecc71;
  --star:#f5b62b;
}
*{box-sizing:border-box;margin:0;padding:0}
html,body{width:1200px;height:4808px;overflow:hidden}
body{background:var(--bg);color:var(--text);font-family:"Inter",sans-serif;font-size:13px;position:relative}
.display{font-family:"Syne",sans-serif;font-weight:800;letter-spacing:-0.5px}
.accent{background:linear-gradient(90deg,var(--blue-900),var(--blue-500));-webkit-background-clip:text;background-clip:text;color:transparent}
section{position:absolute;left:0;width:1200px}
.center{text-align:center}
.eyebrow{font-size:9px;font-weight:700;letter-spacing:1.6px;color:var(--blue-500);text-transform:uppercase;text-align:center}
.eyebrow::before,.eyebrow::after{content:"•";margin:0 7px;font-size:8px}
.section-title{font-size:44px;line-height:50px;text-align:center}
.section-sub{font-size:13px;line-height:24px;color:var(--muted);text-align:center;margin:0 auto}

/* nav */
.nav{top:0;height:52px;display:flex;align-items:center;padding:0 60px;border-bottom:1px solid var(--line-soft)}
.brand{display:flex;align-items:center;gap:9px;font-weight:600;font-size:14px;color:var(--text)}
.brand-mark{width:24px;height:24px;border-radius:6px;background:var(--blue-700)}
.nav-links{display:flex;gap:30px;margin-left:auto;margin-right:auto;padding-left:150px;font-size:11px;color:var(--blue-100)}
.nav-right{display:flex;align-items:center;gap:24px;font-size:11px;color:var(--blue-100)}
.btn{display:inline-flex;align-items:center;justify-content:center;gap:8px;border-radius:6px;font-weight:600;font-size:12px}
.btn-primary{background:linear-gradient(90deg,var(--blue-900),var(--blue-500));color:#fff;box-shadow:0 6px 22px rgba(6,119,186,.35)}
.btn-ghost{border:1px solid var(--line);background:var(--panel);color:#fff}
.nav .btn{height:28px;padding:0 18px;font-size:11px}

/* hero */
.hero{top:52px;height:1030px;background:radial-gradient(ellipse at 50% 20%,rgba(6,84,170,.18),transparent 60%)}
.pill{position:absolute;left:50%;top:43px;transform:translateX(-50%);border:1px solid var(--blue-900);border-radius:20px;padding:5px 14px;font-size:9px;font-weight:700;letter-spacing:1px;color:var(--blue-500);background:rgba(0,84,170,.12)}
.hero h1{position:absolute;top:92px;width:100%;text-align:center;font-size:74px;line-height:80px;letter-spacing:-1px}
.hero-sub{position:absolute;top:266px;width:100%;text-align:center;font-size:14px;line-height:28px;color:var(--muted)}
.hero-actions{position:absolute;top:356px;width:100%;display:flex;justify-content:center;gap:14px}
.hero-actions .btn{height:40px;padding:0 28px}
.stats{position:absolute;top:489px;left:271px;width:657px;height:90px;border:1px solid var(--line);border-radius:10px;background:rgba(12,24,48,.6);display:grid;grid-template-columns:repeat(4,1fr)}
.stat{display:flex;flex-direction:column;align-items:center;justify-content:center;border-right:1px solid var(--line)}
.stat:last-child{border-right:none}
.stat b{font-family:"Syne",sans-serif;font-weight:800;font-size:28px;line-height:32px}
.stat span{font-size:9px;color:var(--muted);margin-top:4px}

.dash{position:absolute;top:644px;left:325px;width:550px;height:343px;border:1px solid var(--line);border-radius:12px;background:var(--panel);box-shadow:0 30px 80px rgba(0,0,0,.5);padding:0 24px}
.dash-bar{height:40px;display:flex;align-items:center;gap:6px;font-size:9px;color:var(--dim)}
.dot{width:8px;height:8px;border-radius:50%}
.dash-tiles{display:grid;grid-template-columns:repeat(3,1fr);gap:14px;margin-top:12px}
.tile{border:1px solid var(--line);border-radius:8px;background:var(--panel-2);height:92px;text-align:center;padding-top:14px}
.tile small{display:block;font-size:8px;font-weight:700;letter-spacing:1px;color:var(--muted)}
.tile b{display:block;font-family:"Syne",sans-serif;font-weight:800;font-size:26px;margin:8px 0 4px}
.tile em{font-style:normal;font-size:8px;color:var(--green)}
.roster{margin-top:14px;border:1px solid var(--line);border-radius:8px;background:var(--panel-2);height:150px;padding:12px 20px}
.roster h4{font-size:8px;letter-spacing:1.2px;color:var(--muted);text-align:center;margin-bottom:12px}
.row{display:flex;align-items:center;height:35px;font-size:10px;font-weight:600}
.avatar{width:22px;height:22px;border-radius:50%;background:var(--blue-700);font-size:8px;display:flex;align-items:center;justify-content:center;margin-right:14px}
.row .name{width:70px}
.track{position:relative;flex:1;height:12px;margin:0 20px 0 0}
.seg{position:absolute;top:0;height:12px;border-radius:3px}
.seg.off{background:#1e2c48}
.seg.on{background:linear-gradient(90deg,var(--blue-900),var(--blue-500))}
.status{font-size:7px;padding:2px 7px;border-radius:8px}
.status.on{color:var(--green);background:rgba(46,204,113,.12)}
.status.rest{color:var(--muted);background:#1e2c48}

/* trusted */
.trusted{top:1128px;height:100px}
.trusted p{font-size:8px;font-weight:700;letter-spacing:1.6px;color:var(--muted);text-align:center}
.logos{display:flex;justify-content:center;gap:28px;margin-top:24px}
.logos span{width:102px;height:22px;border:1px solid var(--line);border-radius:4px;background:var(--panel);font-size:9px;font-weight:700;letter-spacing:1px;color:var(--dim);display:flex;align-items:center;justify-content:center}

/* why */
.why{top:1322px}
.why .section-title{margin-top:22px}
.why .section-sub{margin-top:22px;width:400px}
.cards4{display:grid;grid-template-columns:repeat(4,242px);gap:16px;margin:60px 0 0 93px}
.card{position:relative;border:1px solid var(--line);border-radius:12px;background:linear-gradient(160deg,var(--panel-2),var(--panel));overflow:hidden}
.card::after{content:"";position:absolute;right:-30px;top:-30px;width:90px;height:90px;border-radius:50%;background:radial-gradient(circle,rgba(6,119,186,.25),transparent 70%)}
.cards4 .card{height:237px;padding:30px 26px}
.icon{width:36px;height:36px;border-radius:8px;background:rgba(6,119,186,.2);border:1px solid rgba(6,119,186,.35);display:flex;align-items:center;justify-content:center}
.icon svg{width:16px;height:16px}
.card h3{font-size:15px;font-weight:700;margin:22px 0 12px}
.card p{font-size:11px;line-height:21px;color:var(--muted)}

/* platform */
.platform{top:1977px}
.platform .section-title{margin-top:22px}
.platform .section-sub{margin-top:22px;width:440px}
.fgrid{display:grid;grid-template-columns:650px 318px;gap:18px 16px;margin:44px 0 0 110px}
.fgrid .card{padding:26px;height:283px}
.fgrid .card h3{font-family:"Syne",sans-serif;font-weight:700;font-size:13px;margin:20px 0 12px}
.row2{display:grid;grid-template-columns:318px 316px 318px;gap:16px;margin:18px 0 0 110px}
.row2 .card{height:189px;padding:26px}
.row2 .card h3{font-family:"Syne",sans-serif;font-weight:700;font-size:13px;margin:20px 0 12px}
.chart{margin-top:18px}
.chart div{display:flex;align-items:center;height:19px;font-size:8px;color:var(--muted)}
.chart i{display:block;width:70px}
.chart s{flex:1;height:4px;background:#1e2c48;border-radius:2px;position:relative;text-decoration:none}
.chart s b{position:absolute;left:0;top:0;height:4px;border-radius:2px;background:linear-gradient(90deg,var(--blue-900),var(--blue-500))}
.checks{list-style:none;margin-top:14px}
.checks li{font-size:10px;color:var(--blue-300);height:20px;display:flex;align-items:center;gap:8px}
.checks li::before{content:"";width:6px;height:6px;border-radius:50%;background:var(--blue-500)}

/* industries */
.industries{top:2750px}
.industries .section-title{margin-top:22px}
.industries .section-sub{margin-top:24px}
.tags{display:flex;justify-content:center;gap:10px;margin-top:36px}
.tags span{height:36px;padding:0 20px;border:1px solid var(--line);border-radius:8px;background:var(--panel);font-size:11px;font-weight:600;color:var(--blue-100);display:flex;align-items:center;gap:8px}
.tags span::before{content:"";width:8px;height:8px;border-radius:2px;background:var(--dim)}

/* customers */
.customers{top:3064px}
.customers .section-title{margin-top:22px}
.customers .section-sub{margin-top:24px;width:460px}
.quotes{display:grid;grid-template-columns:repeat(3,327px);gap:18px;margin:52px 0 0 93px}
.quote{height:242px;padding:30px}
.stars{color:var(--star);font-size:11px;letter-spacing:4px}
.quote blockquote{font-size:11.5px;line-height:23px;font-style:italic;color:var(--blue-100);margin-top:14px;height:105px}
.who{display:flex;align-items:center;gap:14px;margin-top:8px}
.who .avatar{width:32px;height:32px;margin:0;font-size:10px;font-weight:700}
.who b{display:block;font-size:11px}
.who small{font-size:9px;color:var(--muted)}

/* pricing */
.pricing{top:3575px}
.pricing .section-title{margin-top:12px;font-size:40px}
.pricing .section-sub{margin-top:8px;font-size:11px}
.plans{display:grid;grid-template-columns:210px 218px 206px;gap:16px;margin:40px 0 0 267px;align-items:start}
.plan{border:1px solid var(--line);border-radius:12px;background:var(--panel);padding:24px;height:286px;margin-top:10px;position:relative}
.plan.pro{height:305px;margin-top:0;border-color:var(--blue-700);background:linear-gradient(170deg,#0d2348,var(--panel))}
.plan .tier{font-size:8px;font-weight:700;letter-spacing:1.2px;color:var(--muted)}
.plan .price{font-family:"Syne",sans-serif;font-weight:800;font-size:32px;margin-top:10px;line-height:36px}
.plan .price small{font-size:13px}
.plan .limit{font-size:8px;color:var(--muted)}
.plan ul{list-style:none;border-top:1px solid var(--line);margin-top:16px;padding-top:12px}
.plan li{font-size:9.5px;color:var(--blue-100);height:23px;display:flex;align-items:center;gap:10px}
.plan li::before{content:"✓";color:var(--green);font-size:10px}
.plan .btn{width:100%;height:32px;margin-top:18px;font-size:10px}
.badge{position:absolute;top:-9px;left:50%;transform:translateX(-50%);background:var(--blue-700);border-radius:10px;padding:3px 12px;font-size:7px;font-weight:700;letter-spacing:1px;white-space:nowrap}

/* cta */
.cta{top:4053px;height:485px;background:linear-gradient(180deg,var(--bg-deep),#071430 60%,var(--bg-deep))}
.cta .eyebrow{margin-top:124px}
.cta .section-title{margin-top:22px;font-size:48px;line-height:54px}
.cta .section-sub{margin-top:26px;width:380px;font-size:12px;line-height:22px}
.cta-actions{display:flex;justify-content:center;gap:12px;margin-top:36px}
.cta-actions .btn{height:34px;padding:0 26px;font-size:11px}

/* footer */
.footer{top:4538px;height:270px;border-top:1px solid var(--line-soft)}
.foot-grid{display:grid;grid-template-columns:355px 196px 196px 196px;margin:64px 0 0 148px}
.foot-grid p{font-size:10px;line-height:18px;color:var(--muted);width:205px;margin-top:16px}
.foot-grid h5{font-size:9px;letter-spacing:1.4px;color:var(--blue-100);margin-bottom:14px}
.foot-grid a{display:block;font-size:10px;color:var(--muted);text-decoration:none;height:23px}
.foot-bottom{position:absolute;top:232px;left:148px;right:148px;display:flex;justify-content:space-between;font-size:8.5px;color:var(--dim)}
.foot-bottom nav{display:flex;gap:22px}
</style>
</head>
<body>

<header class="nav" style="position:absolute;left:0;width:1200px">
  <div class="brand"><span class="brand-mark"></span>Copper Lantern</div>
  <nav class="nav-links"><span>Features</span><span>Industries</span><span>Customers</span><span>Pricing</span></nav>
  <div class="nav-right"><span>Sign in</span><a class="btn btn-primary">Start Free Trial</a></div>
</header>

<section class="hero">
  <div class="pill">✦ AI-POWERED WORKFORCE SCHEDULING</div>
  <h1 class="display">Roster smarter.<br><span class="accent">Run leaner.</span></h1>
  <p class="hero-sub">Copper Lantern automates complex staff scheduling so you can<br>focus on your business — not your spreadsheets.</p>
  <div class="hero-actions">
    <a class="btn btn-primary">Start Free Trial
      <svg width="8" height="8" viewBox="0 0 8 8"><path d="M1 0l6 4-6 4z" fill="#fff"/></svg></a>
    <a class="btn btn-ghost">Book a Demo
      <svg width="10" height="10" viewBox="0 0 10 10"><rect x="1" y="2" width="8" height="7" rx="1" fill="none" stroke="#fff"/><path d="M1 4h8" stroke="#fff"/></svg></a>
  </div>
  <div class="stats">
    <div class="stat"><b>85%</b><span>Less scheduling time</span></div>
    <div class="stat"><b>23%</b><span>Labour cost saved</span></div>
    <div class="stat"><b>12+</b><span>Industries supported</span></div>
    <div class="stat"><b>100%</b><span>Platform uptime</span></div>
  </div>
  <div class="dash">
    <div class="dash-bar"><span class="dot" style="background:#ff5f57"></span><span class="dot" style="background:#febc2e"></span><span class="dot" style="background:#28c840"></span><span style="margin-left:8px">Copper Lantern — Live Dashboard</span></div>
    <div class="dash-tiles">
      <div class="tile"><small>SHIFTS THIS WEEK</small><b>142</b><em>↑ 8% vs last week</em></div>
      <div class="tile"><small>COVERAGE RATE</small><b>98.6%</b><em>↑ Fully optimised</em></div>
      <div class="tile"><small>LABOUR COST</small><b>£14.2k</b><em>↓ £2.1k saved</em></div>
    </div>
    <div class="roster">
      <h4>ROSTER — MON 24 MAR</h4>
      <div class="row"><span class="avatar">JE</span><span class="name">J. Ellison</span>
        <span class="track"><i class="seg off" style="left:0;width:16px"></i><i class="seg on" style="left:22px;width:80px"></i><i class="seg off" style="left:108px;width:40px"></i></span><span class="status on">On shift</span></div>
      <div class="row"><span class="avatar">SN</span><span class="name">S. Navarro</span>
        <span class="track"><i class="seg on" style="left:0;width:50px"></i><i class="seg off" style="left:56px;width:20px"></i><i class="seg on" style="left:82px;width:74px"></i></span><span class="status on">On shift</span></div>
      <div class="row"><span class="avatar">AP</span><span class="name">A. Patel</span>
        <span class="track"><i class="seg off" style="left:0;width:110px"></i><i class="seg on" style="left:116px;width:68px"></i></span><span class="status rest">Rest</span></div>
    </div>
  </div>
</section>

<section class="trusted">
  <p>TRUSTED BY LEADING OPERATIONS TEAMS WORLDWIDE</p>
  <div class="logos"><span>HALVERN</span><span>ORBITA</span><span>KESTREL CO</span><span>LUMERA</span><span>TORVIK</span><span>BRISKA</span></div>
</section>

<section class="why">
  <p class="eyebrow">WHY COPPER LANTERN</p>
  <h2 class="section-title display">Everything you need to run a<br><span class="accent">smart workforce</span></h2>
  <p class="section-sub">Built for operations teams who are tired of juggling rosters in spreadsheets and Chatterbox groups.</p>
  <div class="cards4">
    <div class="card"><div class="icon"><svg viewBox="0 0 16 16"><path d="M9 1L3 9h4l-1 6 6-8H8z" fill="#1a8fe0"/></svg></div>
      <h3>Instant Automation</h3><p>Generate a full week's roster in seconds. AI accounts for availability, skills, contracts, and compliance rules automatically.</p></div>
    <div class="card"><div class="icon"><svg viewBox="0 0 16 16"><path d="M8 1l6 2v5c0 3-3 6-6 7-3-1-6-4-6-7V3z" fill="#1a8fe0"/></svg></div>
      <h3>Compliance Built-In</h3><p>Working time regulations, mandatory rest periods, and union rules are enforced automatically — no manual checks needed.</p></div>
    <div class="card"><div class="icon"><svg viewBox="0 0 16 16"><circle cx="8" cy="8" r="6" fill="#1a8fe0"/><path d="M8 4v8M6 6h3.5M6 10h3.5" stroke="#0c1830" stroke-width="1.3"/></svg></div>
      <h3>Cost Optimisation</h3><p>Cut overtime and avoid under-staffing penalties. Our AI balances cost and coverage so every pound works harder.</p></div>
    <div class="card"><div class="icon"><svg viewBox="0 0 16 16"><circle cx="8" cy="8" r="6" fill="#1a8fe0"/><path d="M6 5v6M10 5v6" stroke="#0c1830" stroke-width="1.5"/></svg></div>
      <h3>Staff Self-Service</h3><p>Employees view shifts, swap, request leave and update availability from the app — reducing manager admin by 60%.</p></div>
  </div>
</section>

<section class="platform">
  <p class="eyebrow">PLATFORM FEATURES</p>
  <h2 class="section-title display">Powerful tools for <span class="accent">every<br>stage</span> of scheduling</h2>
  <p class="section-sub">One platform. Every feature your team needs to schedule smarter, faster, and fairer.</p>
  <div class="fgrid">
    <div class="card"><div class="icon"><svg viewBox="0 0 16 16"><path d="M9 1L3 9h4l-1 6 6-8H8z" fill="#fff"/></svg></div>
      <h3>AI-Powered Auto Scheduling</h3>
      <p>Generate complete, optimised rosters in seconds. The engine accounts for demand forecasts, staff availability, skill requirements, and budget constraints simultaneously.</p>
      <div class="chart">
        <div><i>Mon</i><s><b style="width:82%"></b></s></div>
        <div><i>Tue</i><s><b style="width:94%"></b></s></div>
        <div><i>Wed</i><s><b style="width:71%"></b></s></div>
        <div><i>Thu</i><s><b style="width:88%"></b></s></div>
        <div><i>Fri</i><s><b style="width:96%"></b></s></div>
      </div></div>
    <div class="card"><div class="icon"><svg viewBox="0 0 16 16"><path d="M8 1l6 2v5c0 3-3 6-6 7-3-1-6-4-6-7V3z" fill="#fff"/></svg></div>
      <h3>Compliance Engine</h3>
      <p>Built-in rule sets for UK, EU, and US labour law. Alerts fire before violations happen.</p>
      <ul class="checks"><li>Working Time Directive</li><li>Mandatory rest periods</li><li>Union agreements</li><li>Holiday entitlement</li></ul></div>
  </div>
  <div class="row2">
    <div class="card"><div class="icon"><svg viewBox="0 0 16 16"><circle cx="8" cy="8" r="6" fill="#fff"/><path d="M6.5 5l4 3-4 3z" fill="#0c1830"/></svg></div>
      <h3>Multi-Site Management</h3><p>Manage scheduling across unlimited locations from one central dashboard. Transfer staff between sites with one click.</p></div>
    <div class="card"><div class="icon"><svg viewBox="0 0 16 16"><circle cx="8" cy="8" r="6" fill="none" stroke="#fff" stroke-width="1.5"/><path d="M8 4.5V8l2.5 1.5" stroke="#fff" stroke-width="1.5" fill="none"/></svg></div>
      <h3>Demand Forecasting</h3><p>Connect your sales or booking data. Predict staffing needs before they happen.</p></div>
    <div class="card"><div class="icon"><svg viewBox="0 0 16 16"><circle cx="5.5" cy="5.5" r="2.5" fill="#fff"/><circle cx="11" cy="6" r="2" fill="#fff"/><path d="M1 13c0-3 2-4.5 4.5-4.5S10 10 10 13zM10.5 13c0-2-.5-3-1.2-3.8C10 9 11 9 12 9c2 0 3 1.5 3 4z" fill="#fff"/></svg></div>
      <h3>Staff Self-Service App</h3><p>Shift swaps, leave requests, and availability updates — all handled by staff, not managers.</p></div>
  </div>
</section>

<section class="industries">
  <p class="eyebrow">INDUSTRIES</p>
  <h2 class="section-title display">Built for <span class="accent">every industry</span> with<br>shift-based work</h2>
  <p class="section-sub">Copper Lantern adapts to the unique scheduling demands of your sector.</p>
  <div class="tags"><span>Healthcare</span><span>Retail</span><span>Hospitality</span><span>Logistics</span><span>Manufacturing</span><span>Security</span><span>Events</span><span>Education</span></div>
</section>

<section class="customers">
  <p class="eyebrow">CUSTOMERS</p>
  <h2 class="section-title display">Loved by <span class="accent">operations teams</span><br>worldwide</h2>
  <p class="section-sub">Real results from real teams who switched from spreadsheets to Copper Lantern.</p>
  <div class="quotes">
    <div class="card quote"><div class="stars">★★★★★</div>
      <blockquote>"We cut scheduling time from 4 hours every Sunday to under 10 minutes. The compliance alerts alone have saved us from potential fines twice."</blockquote>
      <div class="who"><span class="avatar">HM</span><div><b>Helen Marsh</b><small>Operations Director, Brookvale Care</small></div></div></div>
    <div class="card quote"><div class="stars">★★★★★</div>
      <blockquote>"The multi-site view is a game changer. Managing 6 locations from one screen used to be a nightmare. Copper Lantern made it effortless."</blockquote>
      <div class="who"><span class="avatar">OP</span><div><b>Owen Pryce</b><small>Head of People, Fernway Retail</small></div></div></div>
    <div class="card quote"><div class="stars">★★★★★</div>
      <blockquote style="height:82px">"Staff morale improved when we introduced fair scheduling. Our team loves the app and we've seen a big drop in no-shows since switching."</blockquote>
      <div class="who"><span class="avatar">ML</span><div><b>Maya Lin</b><small>GM, Harbourline Hotels</small></div></div></div>
  </div>
</section>

<section class="pricing">
  <p class="eyebrow">PRICING</p>
  <h2 class="section-title display">Simple pricing. <span class="accent">No surprises.</span></h2>
  <p class="section-sub">Start free. Scale as you grow. Cancel anytime.</p>
  <div class="plans">
    <div class="plan"><div class="tier">STARTER</div><div class="price">£49<small>/mo</small></div><div class="limit">Up to 25 employees</div>
      <ul><li>Auto-scheduling</li><li>Staff mobile app</li><li>Leave management</li><li>Email support</li></ul>
      <a class="btn btn-ghost">Get started</a></div>
    <div class="plan pro"><span class="badge">MOST POPULAR</span><div class="tier">PROFESSIONAL</div><div class="price">£129<small>/mo</small></div><div class="limit">Up to 100 employees</div>
      <ul><li>Everything in Starter</li><li>Compliance engine</li><li>Multi-site (up to 5)</li><li>Demand forecasting</li><li>Priority support</li></ul>
      <a class="btn btn-primary">Start free trial</a></div>
    <div class="plan"><div class="tier">ENTERPRISE</div><div class="price">Custom</div><div class="limit">Unlimited employees</div>
      <ul><li>Everything in Pro</li><li>Unlimited sites</li><li>API &amp; integrations</li><li>Dedicated CSM</li><li>SLA guarantee</li></ul>
      <a class="btn btn-ghost">Talk to sales</a></div>
  </div>
</section>

<section class="cta">
  <p class="eyebrow">GET STARTED</p>
  <h2 class="section-title display">Ready to transform<br>your workforce?</h2>
  <p class="section-sub">Join thousands of operations teams who have replaced spreadsheets with Copper Lantern. Start your free 14-day trial — no credit card required.</p>
  <div class="cta-actions"><a class="btn btn-primary">Start Free Trial</a><a class="btn btn-ghost">Book a Demo</a></div>
</section>

<footer class="footer" style="position:absolute;left:0;width:1200px">
  <div class="foot-grid">
    <div><div class="brand"><span class="brand-mark"></span>Copper Lantern</div>
      <p>Intelligent workforce scheduling for modern operations teams. Built for simplicity, designed for scale.</p></div>
    <div><h5>PRODUCT</h5><a>Features</a><a>Pricing</a><a>Integrations</a><a>Changelog</a></div>
    <div><h5>INDUSTRIES</h5><a>Healthcare</a><a>Retail</a><a>Hospitality</a><a>Logistics</a></div>
    <div><h5>COMPANY</h5><a>About</a><a>Blog</a><a>Careers</a><a>Contact</a></div>
  </div>
  <div class="foot-bottom"><span>© 2025 Copper Lantern Ltd. All rights reserved.</span><nav><span>Privacy Policy</span><span>Terms</span><span>Cookies</span></nav></div>
</footer>

</body>
</html>
```